Personal Brand Business Card

I am looking for a design that I will use as my personal brand that conveys class (think 1920s gentlemen) and is timeless. I will be putting this on a pearl white, letter pressed, cotton business card.  I’m thinking maybe something with my initials on the front they will flip over for the rest of my information.  But don’t let that limit you.
The information I will have on the back of the business card will be my name, email, and phone number.
Some of the attributes that best describe me are: loyal, dependable, creative, risk taker, open minded, competitive, and empathetic.  I can adapt to my environment quickly and can get along with anyone.  I get excited by figuring out the way things work and finding solutions to problems.

Industry/Entity Type
Business

```html
<!DOCTYPE html>
<html lang="en">
<head>
<meta charset="utf-8">
<title>Graham Whitlock – Business Card Presentation</title>
<link rel="stylesheet" href="https://fonts.googleapis.com/css2?family=Sorts+Mill+Goudy&family=Tinos&display=swap">
<style>
  :root {
    --brown: #523607;
    --band: #4f3304;
    --sheet-light: #ffffff;
    --sheet-dark: #d2d2d2;
    --card-light: #ffffff;
    --card-dark: #cfcfcf;
    --card-edge: #9a9a9a;
    --label: #111111;
  }
  * { margin: 0; padding: 0; box-sizing: border-box; }
  html, body { width: 1200px; height: 720px; overflow: hidden; }
  body {
    position: relative;
    background: radial-gradient(ellipse 70% 65% at 50% 50%, var(--sheet-light) 0%, #f3f3f3 45%, var(--sheet-dark) 100%);
    font-family: "Sorts Mill Goudy", Georgia, serif;
  }
  .band { position: absolute; left: 0; width: 1200px; background: var(--band); }
  .band--top { top: 0; height: 59px; }
  .band--bottom { top: 647px; height: 73px; }

  .card {
    position: absolute;
    top: 177px;
    width: 543px;
    height: 313px;
    border: 2px solid var(--card-edge);
    overflow: hidden;
    background: radial-gradient(ellipse 65% 70% at 50% 45%, var(--card-light) 0%, #f4f4f4 50%, var(--card-dark) 100%);
  }
  .card--front { left: 37px; }
  .card--back { left: 620px; }

  .monogram {
    position: absolute;
    left: 40px;
    top: -52px;
    font-size: 400px;
    line-height: 1;
    letter-spacing: -30px;
    color: var(--brown);
    white-space: nowrap;
  }

  .ornament {
    position: absolute;
    left: 152px;
    width: 258px;
    height: 68px;
    border-radius: 50%;
    background: radial-gradient(ellipse at 50% 50%, rgba(82,54,7,0.55) 0%, rgba(82,54,7,0.25) 55%, rgba(82,54,7,0) 100%);
  }
  .ornament--top { top: 6px; }
  .ornament--bottom { top: 238px; }

  .name {
    position: absolute;
    left: 0; right: 0;
    top: 92px;
    text-align: center;
    font-size: 44px;
    letter-spacing: 1px;
    color: var(--brown);
  }
  .contact {
    position: absolute;
    left: 0; right: 0;
    text-align: center;
    font-size: 21px;
    color: var(--brown);
    display: flex;
    justify-content: center;
    align-items: center;
    gap: 4px;
  }
  .contact--email { top: 148px; }
  .contact--phone { top: 180px; }
  .contact svg { fill: var(--brown); }

  .label {
    position: absolute;
    top: 508px;
    font-family: "Tinos", "Times New Roman", serif;
    font-size: 60px;
    color: var(--label);
    width: 360px;
    text-align: center;
  }
  .label--front { left: 97px; }
  .label--back { left: 727px; }
</style>
</head>
<body>
  <div class="band band--top"></div>

  <section class="card card--front">
    <div class="monogram">GW</div>
  </section>

  <section class="card card--back">
    <div class="ornament ornament--top" role="img" aria-label="Decorative floral flourish"></div>
    <div class="name">Graham Whitlock</div>
    <div class="contact contact--email">
      <svg width="22" height="14" viewBox="0 0 22 14" aria-hidden="true">
        <rect x="0" y="0" width="22" height="14"/>
        <path d="M1 1 L11 8 L21 1" fill="none" stroke="#f4f4f4" stroke-width="1.4"/>
      </svg>
      <span>graham.whitlock@example.com</span>
    </div>
    <div class="contact contact--phone">
      <svg width="18" height="16" viewBox="0 0 18 16" aria-hidden="true">
        <path d="M1 5 Q9 -1 17 5 L15 7 L12 5 L12 3.5 Q9 2.5 6 3.5 L6 5 L3 7 Z"/>
        <path d="M4 8 L14 8 L16 15 L2 15 Z"/>
        <circle cx="9" cy="11.5" r="2" fill="#f4f4f4"/>
      </svg>
      <span>555-014-2287</span>
    </div>
    <div class="ornament ornament--bottom" role="img" aria-label="Decorative floral flourish"></div>
  </section>

  <div class="label label--front">front card</div>
  <div class="label label--back">back card</div>

  <div class="band band--bottom"></div>
</body>
</html>
```